Packaging for Hair Fibers Product

We are a start up company looking for a new packaging design for hair building fibers. These are aimed at predominantly men but also women as well. We already have a logo and i have the packaging design from our competitors. We are wanting to keep the look masculine as 90% of our users will be middle aged men. We would like the colours to be black and white but are open to other colours as well.
It will need to have our logo and the following somewhere on the front.
"Instant Fuller & Thicker Hair" & "Natural Hair Building Fibers" "28g" or "Net Weight 28g"
We only need the front of the packaging designed, please make the other sides of the packaging the same colour but blank.
Target Market(s)
Men 25+
Industry/Entity Type
Hair And Beauty
Requirements
Must have
- Logo which i have included. and the following somewhere on the front.
- "Instant Fuller & Thicker Hair" ; "Natural Hair Building Fibers" "28g" or "Net Weight 28g"
Nice to have
- Make it stand out from the competition or similar to the tarsick example.

```html
<!DOCTYPE html>
<html lang="en">
<head>
<meta charset="utf-8">
<title>Crinalda Hair Building Fibers – Carton Dieline</title>
<link href="https://fonts.googleapis.com/css2?family=Montserrat:wght@300;400;700;800&family=Great+Vibes&display=swap" rel="stylesheet">
<style>
  :root {
    --paper: #ffffff;
    --carton: #000000;
    --ink-light: #ffffff;
    --guide: #8a8a8a;
    --fold: #3a3a3a;
    --dim-text: #111111;
    --band-top: #000000;
    --band-bottom: #d9d9d9;
  }
  html, body {
    margin: 0;
    padding: 0;
    width: 1200px;
    height: 1200px;
    overflow: hidden;
    background: var(--paper);
  }
  .dieline { display: block; width: 1200px; height: 1200px; }
  .carton-part { fill: var(--carton); }
  .fold-line { stroke: var(--fold); stroke-width: 1; fill: none; }
  .guide-line { stroke: var(--guide); stroke-width: 1; fill: none; }
  .dim-label { font-family: "Montserrat", Arial, sans-serif; font-size: 28px; font-weight: 400; fill: var(--dim-text); text-anchor: middle; }
  .front-text { fill: var(--ink-light); text-anchor: middle; }
  .brand-name { font-family: "Montserrat", Arial, sans-serif; font-weight: 300; font-size: 36px; letter-spacing: 5px; }
  .tagline-script { font-family: "Great Vibes", cursive; font-size: 32px; }
  .product-title { font-family: "Montserrat", Arial, sans-serif; font-weight: 700; font-size: 29px; }
  .product-accent { font-family: "Montserrat", Arial, sans-serif; font-weight: 800; font-size: 30px; letter-spacing: 2px; }
  .claim { font-family: "Montserrat", Arial, sans-serif; font-weight: 300; font-size: 20px; }
  .net-label { font-family: "Montserrat", Arial, sans-serif; font-weight: 400; font-size: 16px; }
  .net-value { font-family: "Montserrat", Arial, sans-serif; font-weight: 300; font-size: 23px; }
</style>
</head>
<body>
<svg class="dieline" viewBox="0 0 1500 1500" xmlns="http://www.w3.org/2000/svg">
  <defs>
    <linearGradient id="front-band-fill" x1="0" y1="0" x2="0" y2="1">
      <stop offset="0" stop-color="var(--band-top)"/>
      <stop offset="1" stop-color="var(--band-bottom)"/>
    </linearGradient>
  </defs>

  <g class="dimensions">
    <line class="guide-line" x1="165" y1="78" x2="165" y2="640"/>
    <line class="guide-line" x1="465" y1="78" x2="465" y2="255"/>
    <line class="guide-line" x1="165" y1="107" x2="215" y2="107"/>
    <line class="guide-line" x1="387" y1="107" x2="465" y2="107"/>
    <text class="dim-label" x="302" y="119">5.2 cm</text>

    <line class="guide-line" x1="763" y1="115" x2="763" y2="255"/>
    <line class="guide-line" x1="465" y1="145" x2="540" y2="145"/>
    <line class="guide-line" x1="715" y1="145" x2="763" y2="145"/>
    <text class="dim-label" x="630" y="156">5.2 cm</text>

    <line class="guide-line" x1="70" y1="640" x2="150" y2="640"/>
    <line class="guide-line" x1="70" y1="1192" x2="150" y2="1192"/>
    <line class="guide-line" x1="100" y1="640" x2="100" y2="812"/>
    <line class="guide-line" x1="100" y1="1000" x2="100" y2="1192"/>
    <text class="dim-label" x="100" y="910" transform="rotate(-90 100 910)" dy="10">9.6 cm</text>
  </g>

  <g class="top-flaps">
    <path class="carton-part" d="M165 640 V590 L193 565 V485 Q193 468 215 468 H437 V610 L465 640 Z"/>
    <path class="carton-part" d="M465 640 V272 Q465 255 482 255 H746 Q763 255 763 272 V640 Z"/>
    <path class="carton-part" d="M763 640 L791 610 V468 H1013 Q1035 468 1035 485 V565 L1062 590 V640 Z"/>
  </g>

  <g class="panels">
    <rect class="carton-part" x="165" y="640" width="300" height="552"/>
    <rect class="carton-part" x="465" y="640" width="298" height="552"/>
    <rect class="carton-part" x="763" y="640" width="299" height="552"/>
    <rect class="carton-part" x="1062" y="640" width="300" height="552"/>
    <polygon class="carton-part" points="1362,640 1430,655 1430,1177 1362,1192"/>
  </g>

  <g class="bottom-flaps">
    <polygon class="carton-part" points="165,1192 465,1192 315,1267 315,1335 165,1335"/>
    <polygon class="carton-part" points="465,1192 763,1192 763,1422 680,1422 680,1335 548,1335 548,1422 465,1422"/>
    <polygon class="carton-part" points="763,1192 1062,1192 1062,1335 913,1335 913,1267"/>
    <polygon class="carton-part" points="1062,1192 1362,1192 1278,1335 1278,1422 1145,1422 1145,1335"/>
  </g>

  <g class="folds">
    <line class="fold-line" x1="465" y1="340" x2="763" y2="340"/>
    <line class="fold-line" x1="165" y1="640" x2="1362" y2="640"/>
    <line class="fold-line" x1="165" y1="1192" x2="1362" y2="1192"/>
    <line class="fold-line" x1="465" y1="640" x2="465" y2="1192"/>
    <line class="fold-line" x1="763" y1="640" x2="763" y2="1192"/>
    <line class="fold-line" x1="1062" y1="640" x2="1062" y2="1192"/>
    <line class="fold-line" x1="1362" y1="640" x2="1362" y2="1192"/>
  </g>

  <g class="front-panel">
    <rect class="front-band" x="465" y="1146" width="298" height="30" fill="url(#front-band-fill)" role="img" aria-label="Decorative light accent band along the base of the front panel"/>

    <text class="front-text brand-name" x="614" y="738">CRINALDA</text>

    <text class="front-text tagline-script" x="610" y="845">Natural</text>
    <text class="front-text product-title" x="611" y="886">HAIR BUILDING</text>
    <text class="front-text product-accent" x="612" y="932">FIBERS</text>

    <text class="front-text claim" x="611" y="1020">INSTANT FULLER</text>
    <text class="front-text claim" x="611" y="1049">&amp; THICKER HAIR</text>

    <text class="front-text net-label" x="611" y="1110">Net Weight</text>
    <text class="front-text net-value" x="611" y="1138">28g</text>
  </g>
</svg>
</body>
</html>
```